Roofing Company Truck Wrap Design

We are looking for a clean, modern design for our fleet of trucks. Our trucks are white Varden trucks. We want them to be clean and modern, yet well branded and be able to stand out on the road.
Products and services we want to be written on the truck are:
Tile - Metal - Shingle - Coatings - Flat Roofs
We would want our phone number 505-617-2381, along with our website www.quillbrook-roofing.com.
We also would need our license number reading "BLU #517260".
The orange color in our logo should be pantone 2028C. We would prefer to use a black background behind the logos and phone numbers with white writing so it stands out, with accent colors using the orange from the logo.
Other font styles liked:
- Match font from logo
Colors

```html
<!DOCTYPE html>
<html lang="en">
<head>
<meta charset="utf-8">
<title>Quillbrook Roofing – Truck Wrap</title>
<link rel="stylesheet" href="https://fonts.googleapis.com/css2?family=Montserrat:wght@500;600;800&family=Roboto+Slab:wght@700&display=swap">
<style>
  :root {
    --wrap-red: #e63a2a;
    --wrap-red-deep: #b8261b;
    --wrap-black: #000000;
    --wrap-white: #ffffff;
    --stage: #000000;
  }
  * { margin: 0; padding: 0; box-sizing: border-box; }
  html, body {
    width: 800px;
    height: 1200px;
    overflow: hidden;
    background: var(--stage);
  }
  .canvas {
    position: relative;
    width: 800px;
    height: 1200px;
    background: var(--stage);
  }
  .wrap-panel { position: absolute; display: block; }
  .wrap-panel--side { left: 30px; top: 170px; }
  .wrap-panel--rear { left: 140px; top: 650px; }
  .brand-name {
    font-family: "Roboto Slab", serif;
    font-weight: 700;
    fill: var(--wrap-white);
  }
  .services {
    font-family: "Montserrat", sans-serif;
    font-weight: 800;
    fill: var(--wrap-white);
  }
  .phone {
    font-family: "Montserrat", sans-serif;
    font-weight: 600;
    fill: var(--wrap-white);
  }
  .website {
    font-family: "Montserrat", sans-serif;
    font-weight: 500;
    fill: var(--wrap-white);
  }
  .license {
    font-family: "Montserrat", sans-serif;
    font-weight: 800;
    fill: var(--wrap-white);
  }
</style>
</head>
<body>
<main class="canvas">

  <!-- Side of truck: driver side wrap layout -->
  <svg class="wrap-panel wrap-panel--side" width="740" height="180" viewBox="0 0 740 180" aria-label="Quillbrook Roofing side wrap">
    <defs>
      <linearGradient id="side-red" x1="0" y1="0" x2="1" y2="0">
        <stop offset="0" stop-color="var(--wrap-red)"/>
        <stop offset="0.7" stop-color="var(--wrap-red)"/>
        <stop offset="1" stop-color="var(--wrap-red-deep)"/>
      </linearGradient>
    </defs>
    <rect class="body-field" width="740" height="180" fill="url(#side-red)"/>
    <!-- black chevron band with white keyline -->
    <polygon class="chevron-keyline" points="160,116 290,50 470,128 740,128 740,136 466,136 290,60 160,126" fill="var(--wrap-white)"/>
    <polygon class="chevron-band" points="165,130 290,64 464,140 740,140 740,180 165,180" fill="var(--wrap-black)"/>
    <polygon class="chevron-edge" points="150,120 290,46 296,50 160,124" fill="var(--wrap-black)"/>
    <text class="brand-name" x="290" y="128" font-size="23" text-anchor="middle">Quillbrook Roofing</text>
    <text class="services" x="290" y="150" font-size="7.2" text-anchor="middle">TILE - METAL - SHINGLE - COATINGS - FLAT ROOFS</text>
    <text class="phone" x="405" y="59" font-size="16">505-617-2381</text>
    <text class="website" x="406" y="77" font-size="7">WWW.QUILLBROOK-ROOFING.COM</text>
    <text class="license" x="478" y="126" font-size="6">BLU #517260</text>
  </svg>

  <!-- Tailgate wrap layout -->
  <svg class="wrap-panel wrap-panel--rear" width="510" height="180" viewBox="0 0 510 180" aria-label="Quillbrook Roofing tailgate wrap">
    <defs>
      <linearGradient id="rear-red" x1="0" y1="0" x2="0" y2="1">
        <stop offset="0" stop-color="var(--wrap-red)"/>
        <stop offset="0.6" stop-color="var(--wrap-red)"/>
        <stop offset="1" stop-color="var(--wrap-red-deep)"/>
      </linearGradient>
    </defs>
    <rect class="body-field" width="510" height="180" fill="url(#rear-red)"/>
    <!-- black chevron band with white keyline -->
    <polygon class="chevron-keyline" points="0,156 180,156 362,78 510,150 510,158 362,86 184,164 0,164" fill="var(--wrap-white)"/>
    <polygon class="chevron-band" points="0,168 186,168 362,90 510,162 510,180 0,180" fill="var(--wrap-black)"/>
    <polygon class="chevron-band-top" points="186,168 362,74 510,146 510,162 362,90" fill="var(--wrap-black)"/>
    <text class="brand-name" x="362" y="158" font-size="22" text-anchor="middle">Quillbrook Roofing</text>
    <text class="services" x="362" y="174" font-size="7" text-anchor="middle">TILE - METAL - SHINGLE - COATINGS - FLAT ROOFS</text>
    <text class="phone" x="40" y="75" font-size="17">505-617-2381</text>
    <text class="website" x="41" y="94" font-size="8">WWW.QUILLBROOK-ROOFING.COM</text>
    <text class="license" x="130" y="149" font-size="6">BLU #517260</text>
  </svg>

</main>
</body>
</html>
```